Letterhead Design for Law Firm that Specializes in Property Damage Litigation

We are looking for a redesign of our letterhead. Our current letterhead lists all of our current staff members and we'd like to come up with a design that does NOT list all of the staff members so that it does not need to be updated with every newly hired employee. Must be in editable format.

We are a law firm that specializes in property damage, so we need something that is professional, yet modern. The final design should use our existing logo and should use a blue color scheme (alternate colors would be gray, black, and white).

Industry/Entity Type

Legal

Colors
0054AA
0677BA
7BADD7
CADEEF
E8F1F8

```html
<!DOCTYPE html>
<html lang="en">
<head>
<meta charset="utf-8">
<title>Hartwell Corso &amp; Lindqvist — Letterhead</title>
<link rel="stylesheet" href="https://fonts.googleapis.com/css2?family=Cinzel:wght@400;600&display=swap">
<style>
  :root {
    --backdrop: #808185;
    --paper: #ffffff;
    --ink: #2a2a2a;
    --navy: #1f3a6e;
    --grey: #6d6e71;
  }
  * { margin: 0; padding: 0; box-sizing: border-box; }
  html, body { width: 1200px; height: 831px; overflow: hidden; }
  body {
    background: var(--backdrop);
    font-family: "Cinzel", "Times New Roman", serif;
    color: var(--ink);
    position: relative;
  }
  .sheet {
    position: absolute;
    top: 81px;
    width: 521px;
    height: 673px;
    background: var(--paper);
  }
  .sheet--first { left: 68px; }
  .sheet--second { left: 616px; }

  .office {
    position: absolute;
    top: 42px;
    width: 120px;
    text-align: center;
    font-size: 6.4px;
    line-height: 9.2px;
  }
  .office--pa { left: 41px; }
  .office--nj { left: 349px; }

  .brand {
    position: absolute;
    left: 170px;
    top: 34px;
    width: 170px;
    text-align: center;
  }
  .brand__lockup {
    display: flex;
    align-items: center;
    justify-content: center;
    gap: 8px;
  }
  .brand__mark {
    width: 14px; height: 14px;
    background: var(--navy);
  }
  .brand__name {
    color: var(--navy);
    font-weight: 600;
    font-size: 15.5px;
    line-height: 15px;
    text-align: left;
    letter-spacing: 0.5px;
  }
  .brand__tagline {
    margin-top: 7px;
    font-size: 6.2px;
    letter-spacing: 1.6px;
    color: var(--grey);
  }
  .brand__rule {
    width: 38px;
    height: 1px;
    background: var(--ink);
    margin: 4px auto 3px;
  }
  .brand__contact {
    font-size: 6.8px;
    line-height: 10px;
  }

  .letter {
    position: absolute;
    left: 69px;
    width: 386px;
    font-size: 7.2px;
    line-height: 11px;
    text-transform: lowercase;
  }
  .letter--recipient { top: 157px; }
  .letter--subject { top: 212px; }
  .letter--body { top: 245px; text-align: justify; }
  .letter--body p + p { margin-top: 11px; }
  .letter--closing { top: 444px; }
  .letter--signature { top: 499px; }

  .partners {
    position: absolute;
    left: 0;
    top: 616px;
    width: 100%;
  }
  .partner {
    position: absolute;
    width: 160px;
    margin-left: -80px;
    text-align: center;
  }
  .partner__name { font-size: 7.8px; line-height: 10px; }
  .partner__email { font-size: 6px; color: var(--grey); letter-spacing: 0.3px; }
  .partner--one { left: 100px; }
  .partner--two { left: 262px; }
  .partner--three { left: 422px; top: -1px; }
</style>
</head>
<body>

<section class="sheet sheet--first">
  <div class="office office--pa">
    Philadelphia Office<br>T: 215.555.0140<br>T: 215.555.0188<br>2200 Market Row<br>Suite 840<br>Philadelphia, PA 19107
  </div>
  <header class="brand">
    <div class="brand__lockup">
      <span class="brand__mark"></span>
      <span class="brand__name">Hartwell<br>Corso &amp;<br>Lindqvist</span>
    </div>
    <div class="brand__tagline">THE PROPERTY DAMAGE ATTORNEYS</div>
    <div class="brand__rule"></div>
    <div class="brand__contact">www.hcllegal.com<br>(215) 555-0140</div>
  </header>
  <div class="office office--nj">
    New Jersey Office<br>T: 856.555.0123<br>T: 215.555.0188<br>410 Haddon Crossing<br>Suite 112<br>Cherry Hill, NJ 08002
  </div>

  <div class="letter letter--recipient">Lorem ipsum dolor sit<br>amet, consectetuer<br>adipiscing elit, sed diam</div>
  <div class="letter letter--subject">nonummy nibh euismod tincidunt ut laoreet dolore</div>
  <div class="letter letter--body">
    <p>magna aliquam erat volutpat. Ut wisi enim ad minim veniam, quis nostrud exerci tation ullamcorper suscipit lobortis nisl ut aliquip ex ea commodo consequat. Duis autem vel eum iriure dolor in hendrerit in vulputate velit esse molestie consequat, vel illum dolore eu feugiat nulla facilisis at vero eros et accumsan et iusto odio dignissim qui blandit praesent luptatum zzril delenit augue duis dolore te feugait nulla facilisi.</p>
    <p>Lorem ipsum dolor sit amet, cons ectetuer adipiscing elit, sed diam nonummy nibh euismod tincidunt ut laoreet dolore magna aliquam erat volutpat. Ut wisi enim ad minim veniam, quis nostrud exerci tation ullamcorper suscipit lobortis nisl ut aliquip ex ea commodo consequat.</p>
    <p>Lorem ipsum dolor sit amet, consectetuer adipiscing elit, sed diam nonummy nibh euismod tincidunt ut laoreet dolore magna aliquam erat volutpat. Ut wisi enim ad minim veniam, quis nostrud exerci tation ullamcorper suscipit lobortis nisl ut aliquip ex ea commodo consequat. Duis autem vel eum iriure dolor in hendrerit in vulputate velit esse molestie consequat, vel illum dolore eu feugiat nulla facilisis at vero eros et accumsan et iusto odio</p>
  </div>
  <div class="letter letter--closing">dignissim qui blandi</div>
  <div class="letter letter--signature">praesent luptatum zzril<br>delenit augue duis</div>

  <footer class="partners">
    <div class="partner partner--one"><div class="partner__name">Daniel Hartwell, Esquire</div><div class="partner__email">DHARTWELL@HCLLEGAL.COM</div></div>
    <div class="partner partner--two"><div class="partner__name">Marco Corso, Esquire</div><div class="partner__email">MCORSO@HCLLEGAL.COM</div></div>
    <div class="partner partner--three"><div class="partner__name">Erik Lindqvist, Esquire</div><div class="partner__email">ELINDQVIST@HCLLEGAL.COM</div></div>
  </footer>
</section>

<section class="sheet sheet--second">
  <div class="office office--pa" style="top:40px">
    Philadelphia Office<br>T: 215.555.0140<br>T: 215.555.0188<br>2200 Market Row<br>Suite 840<br>Philadelphia, PA 19107
  </div>
  <header class="brand" style="top:33px">
    <div class="brand__lockup">
      <span class="brand__mark"></span>
      <span class="brand__name">Hartwell<br>Corso &amp;<br>Lindqvist</span>
    </div>
    <div class="brand__tagline">THE PROPERTY DAMAGE ATTORNEYS</div>
    <div class="brand__rule"></div>
    <div class="brand__contact">www.hcllegal.com<br>(215) 555-0140</div>
  </header>
  <div class="office office--nj" style="top:40px">
    New Jersey Office<br>T: 856.555.0123<br>T: 215.555.0188<br>410 Haddon Crossing<br>Suite 112<br>Cherry Hill, NJ 08002
  </div>

  <div class="letter letter--recipient" style="top:156px">Lorem ipsum dolor sit<br>amet, consectetuer<br>adipiscing elit, sed diam</div>
  <div class="letter letter--subject" style="top:211px">nonummy nibh euismod tincidunt ut laoreet dolore</div>
  <div class="letter letter--body" style="top:244px">
    <p>magna aliquam erat volutpat. Ut wisi enim ad minim veniam, quis nostrud exerci tation ullamcorper suscipit lobortis nisl ut aliquip ex ea commodo consequat. Duis autem vel eum iriure dolor in hendrerit in vulputate velit esse molestie consequat, vel illum dolore eu feugiat nulla facilisis at vero eros et accumsan et iusto odio dignissim qui blandit praesent luptatum zzril delenit augue duis dolore te feugait nulla facilisi.</p>
    <p>Lorem ipsum dolor sit amet, cons ectetuer adipiscing elit, sed diam nonummy nibh euismod tincidunt ut laoreet dolore magna aliquam erat volutpat. Ut wisi enim ad minim veniam, quis nostrud exerci tation ullamcorper suscipit lobortis nisl ut aliquip ex ea commodo consequat.</p>
    <p>Lorem ipsum dolor sit amet, consectetuer adipiscing elit, sed diam nonummy nibh euismod tincidunt ut laoreet dolore magna aliquam erat volutpat. Ut wisi enim ad minim veniam, quis nostrud exerci tation ullamcorper suscipit lobortis nisl ut aliquip ex ea commodo consequat. Duis autem vel eum iriure dolor in hendrerit in vulputate velit esse molestie consequat, vel illum dolore eu feugiat nulla facilisis at vero eros et accumsan et iusto odio</p>
  </div>
  <div class="letter letter--closing" style="top:443px">dignissim qui blandi</div>
  <div class="letter letter--signature" style="top:498px">praesent luptatum zzril<br>delenit augue duis</div>

  <footer class="partners" style="top:615px">
    <div class="partner partner--one"><div class="partner__name">Daniel Hartwell, Esquire</div><div class="partner__email">DHARTWELL@HCLLEGAL.COM</div></div>
    <div class="partner partner--two"><div class="partner__name">Marco Corso, Esquire</div><div class="partner__email">MCORSO@HCLLEGAL.COM</div></div>
    <div class="partner partner--three"><div class="partner__name">Erik Lindqvist, Esquire</div><div class="partner__email">ELINDQVIST@HCLLEGAL.COM</div></div>
  </footer>
</section>

</body>
</html>
```